Wholistic Health Clinic (Chiropractic Osteopathic Naturapathic Homeopathic New Website Design

Create a beautiful website for Tallowmere Chiropractic clinic that has been in the Sutherland Shire for over 40 years, that exemplifies the passion for helping people with their health goals using that may include a variety of techniques including Chiropractic, Osteopathy, Acupuncture, Applied Kinesiology, Retained Neonatal Reflexes, Nutritional Advice, Exercise Prescription, Decompression therapy, Massage and Stress management techniques.
We have a wholistic approach that includes Nutritional, Emotional and Physical health

(A more detailed draft will be supplied shortly)

Pages:
Home page
About Us Page
Team Page
Contact page
Terms of service Page
Privacy Page
and any other relevant page(s)

Will supply photos for:
- The Team Page and their qualifications & brief resume
- About Us page

Will supply logos for:
NRB
PLUVEX
VITALOAN
JOBSHIELD
MVA
KPO

Target Market(s)

main target Parents of young children and those 20's to 60's who live in the Sutherland Shire & have disposable income (that said almost everybody would benefit from their services)

Coding

Coded - Design and coding required

Number of Pages Required

5+ page

Font styles to use
Sans Serif

Requirements
Must have
• Please follow the brief

1. Easy to manage ourselves to add alerts (like Covid 19 compliance & Posture fortnight etc.) & update content like photos of team members etc.
2. Must be responsive and look good on mobile devices
3. must be fast loading
4. Logo on every page
5. Easy navigation on every page
6. Phone number must be clickable
7. Terms of service & Privacy pages
8. Slider on page 1 using photo of healthy people of all ages enjoying various lifestyles & ability to add other photos easily
Should not have
• no testimonials or any non compliant elements according to the NRB

```html
<!DOCTYPE html>
<html lang="en">
<head>
<meta charset="utf-8">
<title>Tallowmere Chiropractic – Wholistic Health Clinic</title>
<link href="https://fonts.googleapis.com/css2?family=Roboto:wght@300;400;500;700&display=swap" rel="stylesheet">
<style>
:root{
  --navy:#0a3479;
  --blue:#0d4ea6;
  --mid:#1560bf;
  --sky:#1f80e0;
  --ink:#333;
  --soft:#777;
  --grey:#f2f3f5;
  --line:#d6dbe3;
  --white:#fff;
}
*{box-sizing:border-box;margin:0;padding:0}
html,body{width:1200px;height:4364px;overflow:hidden}
body{font-family:'Roboto',Arial,sans-serif;color:var(--ink);background:var(--white);position:relative}
a{color:inherit;text-decoration:none}

/* header */
.site-header{position:absolute;top:0;left:0;width:1200px;height:70px;display:flex;align-items:center;justify-content:space-between;padding:0 70px;z-index:3}
.brand{display:flex;align-items:center;gap:10px;color:var(--white);font-weight:500;font-size:17px}
.brand-dot{width:30px;height:30px;border-radius:50%;background:var(--white);opacity:.9}
.brand small{display:block;font-size:9px;font-weight:400;letter-spacing:.5px}
.main-nav{display:flex;gap:6px}
.main-nav a{color:var(--white);font-size:15px;padding:10px 18px}
.main-nav a.active{border-bottom:2px solid var(--white)}

/* hero */
.hero{position:absolute;top:0;left:0;width:1200px;height:640px;background:linear-gradient(180deg,#6f9fd0 0%,#a9c7e6 55%,#8fb36a 82%,#5f8a3e 100%)}
.hero-tagline{position:absolute;top:60px;left:320px;width:560px;padding:12px 20px;background:rgba(10,52,121,.55);color:var(--white);font-size:26px;font-weight:500;text-align:center}
.hero-arrow{position:absolute;top:330px;width:30px;height:30px}
.hero-arrow.prev{left:70px}.hero-arrow.next{right:70px}

/* intro boxes */
.intro-boxes{position:absolute;top:610px;left:180px;width:840px;display:flex;gap:20px;z-index:2}
.intro-box{flex:1;height:250px;padding:24px 28px;color:var(--white);text-align:center}
.intro-box:nth-child(1){background:var(--navy)}
.intro-box:nth-child(2){background:var(--mid)}
.intro-box:nth-child(3){background:var(--sky)}
.intro-box h2{font-size:21px;font-weight:700;margin-bottom:14px}
.intro-box p{font-size:12.5px;line-height:1.45;text-align:left}
.btn-small{display:inline-block;margin-top:16px;padding:5px 14px;border:1px solid var(--white);font-size:12px;color:var(--white)}

/* about */
.section-title{text-align:center;color:var(--blue);font-size:30px;font-weight:500;letter-spacing:1px;display:flex;align-items:center;justify-content:center;gap:18px}
.section-title::before,.section-title::after{content:"";width:80px;height:1px;background:var(--line)}
.about{position:absolute;top:905px;left:0;width:1200px}
.about p{width:1000px;margin:28px auto 0;font-size:15px;line-height:1.6;color:var(--soft);text-align:center}

/* services band */
.services{position:absolute;top:1110px;left:0;width:1200px;height:620px;background:var(--blue)}
.service-list{display:flex;gap:50px;justify-content:center;padding-top:30px}
.service{width:250px;text-align:center;color:var(--white)}
.service .photo{height:230px;border-radius:4px}
.service:nth-child(2) .photo{background:linear-gradient(160deg,#f3ede6,#d9c8b6)}
.service:nth-child(1) .photo{background:linear-gradient(160deg,#f7f7f7,#d0b99a)}
.service:nth-child(3) .photo{background:linear-gradient(160deg,#e9ded3,#b9957a)}
.service h3{font-size:21px;font-weight:400;margin:26px 0 16px;line-height:1.25;min-height:52px}
.service p{font-size:13px;line-height:1.5;text-align:left}
.btn-light{display:inline-block;margin-top:20px;padding:8px 36px;background:var(--white);color:var(--blue);font-size:14px}
.band-arrow{position:absolute;top:300px;width:26px;height:40px}
.band-arrow.prev{left:40px}.band-arrow.next{right:40px}

/* team */
.team{position:absolute;top:1770px;left:0;width:1200px}
.team-list{display:flex;gap:30px;justify-content:center;margin-top:34px}
.team-card{width:262px;height:440px;border:2px solid #bcd3f0;border-radius:12px;text-align:center;padding:32px 24px}
.avatar{width:150px;height:150px;margin:0 auto;border-radius:50%;background:linear-gradient(180deg,#e5eaf0,#c9d3df)}
.team-card h3{margin-top:34px;font-size:14px;font-weight:500;color:var(--soft);line-height:1.4}
.team-card:nth-child(2) h3{color:var(--blue)}
.team-card p{margin-top:14px;font-size:12.5px;line-height:1.45;color:var(--soft)}
.btn-view{display:inline-block;margin-top:16px;padding:3px 28px;border:1px solid var(--blue);color:var(--blue);font-size:13px;letter-spacing:2px;font-weight:500}
.team-arrow{position:absolute;top:270px;width:22px;height:40px}
.team-arrow.prev{left:90px}.team-arrow.next{right:90px}
.dots{display:flex;gap:6px;justify-content:center;margin-top:16px}
.dots span{width:7px;height:7px;border-radius:50%;background:#bbb}
.dots span:first-child{background:var(--blue)}

/* pillars */
.pillar{position:absolute;left:0;width:1200px;display:flex;align-items:center;gap:60px;padding:0 180px}
.pillar h2{color:var(--blue);font-size:28px;font-weight:500;margin-bottom:16px}
.pillar p{font-size:13px;line-height:1.55;color:var(--soft)}
.pillar .more{display:block;margin-top:12px;font-size:13px;color:var(--soft)}
.pillar .text{flex:1}
.pillar .photo{width:380px;height:230px;flex:none}
.nutrition{top:2400px;height:290px;background:var(--grey)}
.nutrition .photo{background:linear-gradient(135deg,#f5f0e6,#c8d68a 50%,#e08a4f)}
.emotions{top:2720px;height:300px}
.emotions .photo{background:linear-gradient(135deg,#e7d4ef,#b991d1)}
.exercise{top:3030px;height:250px;background:var(--grey)}
.exercise .photo{height:220px;background:linear-gradient(180deg,#d9b878,#8d9b5a)}

/* alert */
.alert{position:absolute;top:3300px;left:0;width:1200px;height:230px;background:linear-gradient(90deg,#082a62,#0d4ea6 50%,#082a62);color:var(--white);text-align:center;padding-top:42px}
.alert h2{font-size:28px;font-weight:500;margin-bottom:18px}
.alert p{width:700px;margin:0 auto;font-size:15px;line-height:1.5}

/* partners */
.partners{position:absolute;top:3580px;left:0;width:1200px;display:flex;justify-content:center;gap:36px;align-items:center}
.badge{width:110px;height:64px;border-radius:6px;background:#e3e8ef}
.badge.dark{background:#2a4d86}
.badge.round{width:70px;border-radius:50%}

/* footer */
.site-footer{position:absolute;top:3760px;left:0;width:1200px;height:540px;background:linear-gradient(180deg,#eef2f7,#dde6f1);padding:60px 90px;display:flex;gap:110px}
.footer-brand{width:280px}
.footer-brand .brand{color:var(--blue)}
.footer-brand .brand-dot{background:var(--blue)}
.footer-brand h4{margin-top:40px;font-size:15px;font-weight:500;color:var(--blue)}
.footer-brand p{margin-top:8px;font-size:14px;line-height:1.6}
.footer-col h4{font-size:15px;font-weight:500;color:var(--blue);margin-bottom:16px;margin-top:80px}
.footer-col li{list-style:none;font-size:14px;line-height:2.1}
.contact-line{display:flex;gap:8px;align-items:center;font-size:14px;line-height:1.8}
.socials{display:flex;gap:10px;margin-top:14px}
.socials span{width:18px;height:18px;border-radius:3px;background:var(--blue)}
.copyright{position:absolute;top:4300px;left:0;width:1200px;height:64px;background:var(--navy);color:var(--white);font-size:13px;display:flex;align-items:center;justify-content:center}
</style>
</head>
<body>

<section class="hero" role="img" aria-label="Slider photo of healthy people jumping in a field under a blue sky"></section>

<header class="site-header">
  <a class="brand" href="#"><span class="brand-dot"></span><span>Tallowmere Chiropractic<small>WHOLISTIC HEALTH CLINIC</small></span></a>
  <nav class="main-nav">
    <a class="active" href="#">Home</a><a href="#">About us</a><a href="#">Team</a><a href="#">Services</a><a href="#">Contact</a>
  </nav>
</header>

<div class="hero-tagline">"Time to book in for a chiropractic or massage treatment today"</div>
<svg class="hero-arrow prev" viewBox="0 0 30 30"><path d="M20 4 8 15l12 11" fill="none" stroke="#fff" stroke-width="3"/></svg>
<svg class="hero-arrow next" viewBox="0 0 30 30"><path d="M10 4l12 11-12 11" fill="none" stroke="#fff" stroke-width="3"/></svg>

<div class="intro-boxes">
  <article class="intro-box"><h2>WHO WE ARE</h2><p>Tallowmere Chiropractic, situated in the Shire and established for over 40 years, is passionate about helping you achieve your health goals. We take a unique approach, understand you as an individual, and tailor treatment accordingly.</p><a class="btn-small" href="#">View More</a></article>
  <article class="intro-box"><h2>WHAT WE DO</h2><p>Tallowmere Chiropractic, situated in the Shire and established for over 40 years, is passionate about helping you achieve your health goals. We take a unique approach, understand you as an individual, and tailor treatment accordingly.</p><a class="btn-small" href="#">View More</a></article>
  <article class="intro-box"><h2>WHAT TO EXPECT</h2><p>Tallowmere Chiropractic, situated in the Shire and established for over 40 years, is passionate about helping you achieve your health goals. We take a unique approach, understand you as an individual, and tailor treatment accordingly.</p><a class="btn-small" href="#">View More</a></article>
</div>

<section class="about">
  <h2 class="section-title">ABOUT US</h2>
  <p>At Tallowmere Chiropractic we place great importance on the correct foods and nutritional supplements for optimal health and wellbeing. Different bodies, at different stages of life, require different nutritional needs. Get educated on the best nutrition for your requirements. At Tallowmere Chiropractic we place great importance on the correct foods and nutritional supplements for optimal health and wellbeing. Different bodies, at different stages of life require different nutritional needs. Get educated on the best nutrition for your requirements.</p>
</section>

<section class="services">
  <svg class="band-arrow prev" viewBox="0 0 26 40"><path d="M20 4 6 20l14 16" fill="none" stroke="#fff" stroke-width="3"/></svg>
  <svg class="band-arrow next" viewBox="0 0 26 40"><path d="M6 4l14 16L6 36" fill="none" stroke="#fff" stroke-width="3"/></svg>
  <div class="service-list">
    <article class="service"><div class="photo" role="img" aria-label="Diagram of applied kinesiology meridian points around a human figure"></div><h3>APPLIED<br>KINESIOLOGY</h3><p>Why would my baby or child need Chiropractic care? The way a baby is positioned during pregnancy and birth, naturally or by caesarean, can affect their spine, and everyday falls and knocks add up.</p><a class="btn-light" href="#">View More</a></article>
    <article class="service"><div class="photo" role="img" aria-label="Photo of a pregnant woman holding her belly"></div><h3>CHIROPRACTIC CARE DURING PREGNANCY</h3><p>Using modified pregnancy specific techniques, spinal and joint problems can be treated and may help to reduce discomfort, pain and reduce correct nerve signal, needed for mother and baby.</p><a class="btn-light" href="#">View More</a></article>
    <article class="service"><div class="photo" role="img" aria-label="Photo of a person receiving acupuncture needles"></div><h3>ACUPUNCTURE AND DRY NEEDLING</h3><p>Acupuncture is based on the ancient Chinese premise that pain or illness results when energy and blood in the body cannot move freely through its meridians. The application of needles helps.</p><a class="btn-light" href="#">View More</a></article>
  </div>
</section>

<section class="team">
  <h2 class="section-title">OUR TEAM</h2>
  <svg class="team-arrow prev" viewBox="0 0 22 40"><path d="M18 4 4 20l14 16" fill="none" stroke="#bbb" stroke-width="3"/></svg>
  <svg class="team-arrow next" viewBox="0 0 22 40"><path d="M4 4l14 16L4 36" fill="none" stroke="#bbb" stroke-width="3"/></svg>
  <div class="team-list">
    <article class="team-card"><div class="avatar" role="img" aria-label="Portrait photo of team member"></div><h3>DR OWEN MARSH DC, DO (CHIROPRACTOR, OSTEOPATH)</h3><p>Owen graduated with honours from his chiropractic degree and has worked in the Shire for many years. He is a Chiropractor and Osteopath and has studied widely.</p><a class="btn-view" href="#">VIEW</a></article>
    <article class="team-card"><div class="avatar" role="img" aria-label="Portrait photo of team member"></div><h3>DR CLARA BENN B.SC., M.CHIRO (CHIROPRACTOR)</h3><p>Clara graduated with a Bachelor of Science and a Master of Chiropractic. For seven years prior to this she was in the sports and health sector.</p><a class="btn-view" href="#">VIEW</a></article>
    <article class="team-card"><div class="avatar" role="img" aria-label="Portrait photo of team member"></div><h3>DR NINA REYES B.SC., M.CHIRO (CHIROPRACTOR)</h3><p>Nina is a warm and caring person who graduated with a Bachelor of Chiropractic Science and a Master's Degree in Chiropractic in 2004.</p><a class="btn-view" href="#">VIEW</a></article>
  </div>
  <div class="dots"><span></span><span></span></div>
</section>

<section class="pillar nutrition">
  <div class="text"><h2>NUTRITION</h2><p>At Tallowmere Chiropractic we place great importance on the correct foods and nutritional supplements for optimal health and wellbeing. Different bodies, at different stages of life require different nutritional needs. Get educated on the best nutrition for your requirements.</p><a class="more" href="#">Read more</a></div>
  <div class="photo" role="img" aria-label="Photo of fresh fruit and vegetables"></div>
</section>

<section class="pillar emotions">
  <div class="photo" role="img" aria-label="Photo of fingertips with drawn emotion expressions"></div>
  <div class="text"><h2>EMOTIONS</h2><p>At Tallowmere Chiropractic we place great importance on the correct foods and nutritional supplements for optimal health and wellbeing. Different bodies, at different stages of life require different nutritional needs. Get educated on the best nutrition for your requirements.</p><a class="more" href="#">Read more</a></div>
</section>

<section class="pillar exercise">
  <div class="text"><h2>EXERCISE</h2><p>At Tallowmere Chiropractic we place great importance on the correct foods and nutritional supplements for optimal health and wellbeing. Different bodies, at different stages of life require different nutritional needs. Get educated on the best nutrition for your requirements.</p><a class="more" href="#">Read more</a></div>
  <div class="photo" role="img" aria-label="Photo of a person stretching outdoors at sunset"></div>
</section>

<section class="alert">
  <h2>COVID - 19 Alert</h2>
  <p>At Tallowmere Chiropractic we place great importance on the correct foods and nutritional supplements for optimal health and wellbeing. Different bodies, at different stages of life require different nutritional needs. Get educated on the best nutrition for your requirements.</p>
</section>

<div class="partners" aria-label="Partner and registration badges">
  <span class="badge dark"></span><span class="badge"></span><span class="badge round"></span><span class="badge"></span><span class="badge dark"></span><span class="badge dark"></span>
</div>

<footer class="site-footer">
  <div class="footer-brand">
    <a class="brand" href="#"><span class="brand-dot"></span><span>Tallowmere Chiropractic<small>WHOLISTIC HEALTH CLINIC</small></span></a>
    <h4>CLINIC HOURS</h4>
    <p>MON to FRI<br>2.30 pm - 6.45 pm</p>
    <p>SAT : 8 am - 12 pm</p>
  </div>
  <div class="footer-col">
    <h4>Quick Links</h4>
    <ul><li>About Us</li><li>Team</li><li>Contact</li><li>Terms and Conditions</li><li>Privacy Policy</li></ul>
  </div>
  <div class="footer-col">
    <h4>Contact Us</h4>
    <div class="contact-line"><svg width="14" height="14" viewBox="0 0 24 24"><path d="M6.6 10.8a15 15 0 0 0 6.6 6.6l2.2-2.2c.3-.3.7-.4 1-.2 1.1.4 2.3.6 3.6.6.6 0 1 .4 1 1V20c0 .6-.4 1-1 1A17 17 0 0 1 3 4c0-.6.4-1 1-1h3.5c.6 0 1 .4 1 1 0 1.3.2 2.5.6 3.6.1.3 0 .7-.2 1z" fill="#0d4ea6"/></svg><span>02 9000 4181<br>0400 555 017</span></div>
    <div class="contact-line"><svg width="14" height="14" viewBox="0 0 24 24"><path d="M2 5h20v14H2z M2 5l10 8 10-8" fill="none" stroke="#0d4ea6" stroke-width="2"/></svg><span>hello@tallowmere.example</span></div>
    <div class="socials"><span></span><span></span><span></span></div>
  </div>
</footer>

<div class="copyright">© tallowmerechiropractic.example 2020 All rights reserved.</div>

</body>
</html>
```